Postcard Design Project

Underground fencing for dogs (Invisible dog fencing) a postcard for my customers
"Keeping in touch with them" offering them $25.00 service call/ $75.00 install I My Logo on my truck/paper work is the Girl & Dog touching noises.

Fencing

```html
<!DOCTYPE html>
<html lang="en">
<head>
<meta charset="utf-8">
<title>Hollow Brook Pet Containment – Spring Savings Postcard</title>
<link href="https://fonts.googleapis.com/css2?family=Oswald:wght@500;700&family=Roboto+Condensed:wght@400;700&family=Permanent+Marker&family=Cormorant+Garamond:wght@700&display=swap" rel="stylesheet">
<style>
  :root {
    --backdrop: #e4e4e4;
    --teal: #1fa58a;
    --ink-dark: #2a2228;
    --panel-top: #ecd92a;
    --panel-bottom: #78b35c;
    --offer-red: #e3151b;
    --cta-orange: #f7941d;
    --white: #ffffff;
    --text-dark: #2b2b2b;
    --photo-grass: #5f8e3a;
    --photo-trees: #3f5d2a;
    --photo-dog: #4a3428;
  }
  * { margin: 0; padding: 0; box-sizing: border-box; }
  html, body { width: 1200px; height: 1200px; overflow: hidden; }
  body { background: var(--backdrop); position: relative; }

  .postcard {
    position: absolute; left: 210px; top: 25px;
    width: 780px; height: 1150px; overflow: hidden;
    background: var(--teal);
  }
  .postcard-art { position: absolute; inset: 0; }

  .burst-text {
    position: absolute; left: 58px; top: 62px; width: 210px;
    font-family: "Permanent Marker", cursive;
    font-size: 44px; line-height: 0.98; color: var(--white);
    text-align: center; transform: rotate(-14deg);
    text-shadow: 2px 2px 0 rgba(0,0,0,.35);
  }

  .offer {
    position: absolute; border-radius: 50%;
    background: radial-gradient(circle at 50% 45%, #ffffff 30%, #d9d9d9 65%, #8f8f8f 100%);
    border: 8px solid var(--white);
    box-shadow: 0 4px 12px rgba(0,0,0,.35);
    display: flex; flex-direction: column; align-items: center; justify-content: center;
    text-align: center;
    font-family: "Roboto Condensed", sans-serif; color: var(--text-dark);
  }
  .offer-service { left: 526px; top: 148px; width: 214px; height: 214px; }
  .offer-install { left: 406px; top: 376px; width: 244px; height: 244px; }
  .offer-amount {
    font-family: "Oswald", sans-serif; font-weight: 700; color: var(--offer-red);
    font-size: 48px; line-height: 1; margin-bottom: 6px;
  }
  .offer-amount small { font-size: 34px; }
  .offer-detail { font-size: 18px; line-height: 1.25; text-transform: uppercase; }

  .tagline {
    position: absolute; left: 50px; top: 522px; width: 180px;
    font-family: "Oswald", sans-serif; font-weight: 700;
    font-size: 38px; line-height: 1.14; color: var(--white);
    text-transform: uppercase; text-align: right;
    text-shadow: 2px 2px 3px rgba(0,0,0,.6);
    letter-spacing: -0.5px;
  }

  .service-lines {
    position: absolute; left: 240px; top: 630px; width: 500px;
    font-family: "Roboto Condensed", sans-serif; font-weight: 700;
    color: var(--ink-dark); line-height: 1.3;
  }
  .service-lines span { display: block; }
  .service-lines .line-1 { font-size: 40px; padding-left: 124px; }
  .service-lines .line-2 { font-size: 36px; padding-left: 84px; }
  .service-lines .line-3 { font-size: 40px; }

  .brand-mark {
    position: absolute; left: 30px; top: 750px; width: 222px; height: 222px;
    border-radius: 50%; border: 10px solid var(--white);
    background: radial-gradient(circle at 40% 45%, #f3d6bd 0%, #c9a070 45%, #5a4a3a 100%);
  }
  .brand-name {
    position: absolute; left: 268px; top: 852px;
    font-family: "Roboto Condensed", sans-serif; font-weight: 700; color: var(--white);
  }
  .brand-name .brand-main { display: block; font-size: 70px; line-height: 1; letter-spacing: 1px; }
  .brand-name .brand-sub { display: block; font-size: 32px; line-height: 1.2; letter-spacing: 7px; font-weight: 400; }

  .info-band {
    position: absolute; left: 0; top: 972px; width: 780px; height: 150px;
    background: var(--ink-dark); color: var(--white); text-align: center;
  }
  .experience {
    margin-top: 30px;
    font-family: "Cormorant Garamond", serif; font-weight: 700;
    font-variant: small-caps; font-size: 30px; letter-spacing: 0.5px;
  }
  .call-to-action {
    margin-top: 4px;
    font-family: "Oswald", sans-serif; font-weight: 700; font-size: 38px;
    text-transform: uppercase; letter-spacing: -0.5px;
  }
  .call-to-action .estimate, .call-to-action .phone { color: var(--cta-orange); }
</style>
</head>
<body>
  <article class="postcard">
    <svg class="postcard-art" width="780" height="1150" viewBox="0 0 780 1150" xmlns="http://www.w3.org/2000/svg">
      <defs>
        <linearGradient id="photoTone" x1="0" y1="0" x2="0" y2="1">
          <stop offset="0" stop-color="var(--photo-trees)"/>
          <stop offset="0.3" stop-color="#6f7d60"/>
          <stop offset="0.55" stop-color="var(--photo-dog)"/>
          <stop offset="1" stop-color="var(--photo-grass)"/>
        </linearGradient>
        <linearGradient id="panelTone" x1="0" y1="0" x2="0" y2="1">
          <stop offset="0" stop-color="var(--panel-top)"/>
          <stop offset="1" stop-color="var(--panel-bottom)"/>
        </linearGradient>
        <linearGradient id="burstTone" x1="0" y1="0" x2="0" y2="1">
          <stop offset="0" stop-color="#e6e02a"/>
          <stop offset="1" stop-color="#2fa27a"/>
        </linearGradient>
      </defs>

      <rect class="photo-area" x="0" y="0" width="780" height="800" fill="url(#photoTone)"
            role="img" aria-label="Photo of a brown pointer dog with an orange collar sitting on a lawn, a service van parked behind"/>

      <path class="divider-stripe" d="M655 0 L780 0 L780 800 L0 800 L0 790 C120 730 260 660 360 540 C470 410 560 250 655 0 Z" fill="var(--ink-dark)"/>
      <path class="offer-panel" d="M695 0 L780 0 L780 800 L20 800 C150 730 280 660 390 530 C480 420 580 280 695 0 Z" fill="url(#panelTone)"/>

      <path class="brand-band" d="M0 758 C250 830 520 830 780 740 L780 1150 L0 1150 Z" fill="var(--teal)"/>

      <polygon class="spring-burst" transform="translate(160 125) scale(1.12)" fill="url(#burstTone)"
        points="100,0 82.4,16.4 92.4,38.3 69.8,46.7 70.7,70.7 46.7,69.8 38.3,92.4 16.4,82.4 0,100 -16.4,82.4 -38.3,92.4 -46.7,69.8 -70.7,70.7 -69.8,46.7 -92.4,38.3 -82.4,16.4 -100,0 -82.4,-16.4 -92.4,-38.3 -69.8,-46.7 -70.7,-70.7 -46.7,-69.8 -38.3,-92.4 -16.4,-82.4 0,-100 16.4,-82.4 38.3,-92.4 46.7,-69.8 70.7,-70.7 69.8,-46.7 92.4,-38.3 82.4,-16.4"/>
    </svg>

    <div class="burst-text">Spring Savings!</div>

    <div class="offer offer-service">
      <div class="offer-amount">25% <small>OFF</small></div>
      <div class="offer-detail">Service<br>calls repairs<br>maintenance</div>
    </div>

    <div class="offer offer-install">
      <div class="offer-amount">75$ <small>OFF</small></div>
      <div class="offer-detail">Complete<br>pet containment<br>system installation</div>
    </div>

    <div class="tagline">Your pet’s<br>safety<br>is our<br>priority!</div>

    <div class="service-lines">
      <span class="line-1">Veterinarian Approved</span>
      <span class="line-2">Underground Fencing &amp;</span>
      <span class="line-3">Training for Your Dog</span>
    </div>

    <div class="brand-mark" role="img" aria-label="Company mark photo: a woman and a puppy touching noses"></div>
    <div class="brand-name">
      <span class="brand-main">HOLLOW BROOK</span>
      <span class="brand-sub">PET CONTAINMENT</span>
    </div>

    <section class="info-band">
      <p class="experience">Most Experienced in Fairfield County since 1995</p>
      <p class="call-to-action"><span class="estimate">Free Estimates!</span> Call us now <span class="phone">(555) 014-2870</span></p>
    </section>
  </article>
</body>
</html>
```